Awesome Design for a psychotherapy practise

We need a simple but modern design for a psychotherapy practise which opened recently. A logo, letterhead and a business card. Maybe something with the greek letter psi.

Font styles to use
Serif
Sans Serif

```html
<!DOCTYPE html>
<html lang="en">
<head>
<meta charset="UTF-8">
<title>Psychotherapy Practice Letterhead</title>
<link href="https://fonts.googleapis.com/css2?family=Montserrat:ital,wght@0,400;0,500;0,600;0,700;1,500&display=swap" rel="stylesheet">
<style>
  :root {
    --brand-blue: #0a4c82;
    --ink: #3c3c3e;
    --body-text: #444446;
    --band-dark: #3f3f42;
    --paper: #ffffff;
    --shade: #e6e7e9;
  }
  * { margin: 0; padding: 0; box-sizing: border-box; }
  html, body { width: 900px; height: 1200px; overflow: hidden; background: var(--paper); }
  body { font-family: "Montserrat", Arial, sans-serif; color: var(--body-text); }
  .letterhead { position: relative; width: 900px; height: 1200px; overflow: hidden; background: var(--paper); }
  .backdrop { position: absolute; inset: 0; width: 900px; height: 1200px; }
  .letter-date { position: absolute; left: 570px; top: 277px; font-size: 17.5px; font-weight: 500; color: var(--ink); letter-spacing: 0.3px; }
  .practice-title { position: absolute; left: 118px; top: 314px; font-size: 28px; font-weight: 700; line-height: 1.15; letter-spacing: -0.3px; }
  .practice-title .line-primary { display: block; color: var(--brand-blue); }
  .practice-title .line-secondary { display: block; color: var(--ink); }
  .letter-body { position: absolute; left: 120px; top: 410px; width: 663px; font-size: 16.3px; line-height: 31.6px; text-align: justify; font-weight: 500; letter-spacing: 0.2px; }
  .letter-body p + p { margin-top: 31.6px; }
  .contact-list { position: absolute; left: 120px; top: 925px; list-style: none; }
  .contact-list li { display: flex; align-items: center; height: 27.5px; font-size: 13.5px; font-weight: 600; color: var(--ink); }
  .contact-list svg { width: 15px; height: 15px; margin-right: 14px; fill: var(--brand-blue); }
  .signature { position: absolute; right: 126px; top: 932px; text-align: right; }
  .signature .signer-name { font-size: 18px; font-weight: 700; color: var(--ink); letter-spacing: 0.4px; }
  .signature .signer-role { font-size: 18px; font-style: italic; font-weight: 500; color: var(--ink); margin-top: 2px; letter-spacing: 0.4px; }
  .signature .signer-note { font-size: 14px; font-weight: 700; color: var(--brand-blue); margin-top: 6px; }
</style>
</head>
<body>
<main class="letterhead">
  <svg class="backdrop" viewBox="0 0 900 1200" aria-hidden="false">
    <defs>
      <linearGradient id="photoTone" x1="0" y1="0" x2="1" y2="1">
        <stop offset="0" stop-color="#c9d4e0"/>
        <stop offset="0.5" stop-color="#9fb2c6"/>
        <stop offset="1" stop-color="#6f87a1"/>
      </linearGradient>
      <linearGradient id="shadeTop" x1="0" y1="0" x2="1" y2="0.4">
        <stop offset="0" stop-color="#d9dbde"/>
        <stop offset="1" stop-color="#ffffff" stop-opacity="0"/>
      </linearGradient>
      <linearGradient id="shadeLow" x1="0" y1="1" x2="0.3" y2="0">
        <stop offset="0" stop-color="#e1e2e5"/>
        <stop offset="1" stop-color="#ffffff" stop-opacity="0"/>
      </linearGradient>
    </defs>
    <g class="facets-top">
      <polygon points="536,0 620,0 590,90 500,330 510,300" fill="url(#shadeTop)"/>
      <polygon points="620,0 900,0 900,110 700,360 510,300" fill="url(#shadeTop)" opacity="0.8"/>
      <polygon points="700,0 900,0 900,40 640,350 600,330" fill="#eef0f2" opacity="0.7"/>
    </g>
    <g class="facets-low">
      <polygon points="300,860 420,830 230,1200 110,1200" fill="url(#shadeLow)"/>
      <polygon points="180,960 280,900 190,1200 60,1200" fill="url(#shadeLow)" opacity="0.7"/>
    </g>
    <polygon class="hero-photo" role="img" aria-label="Photo of a therapist with clipboard listening to a client on a sofa" points="0,0 536,0 433,258 0,258" fill="url(#photoTone)"/>
    <polygon class="band-dark" points="213,1154 662,1154 638,1200 188,1200" fill="var(--band-dark)"/>
    <polygon class="band-blue" points="660,1110 900,1110 900,1200 625,1200" fill="var(--brand-blue)"/>
  </svg>

  <p class="letter-date">Date: 24 October 2035</p>

  <h1 class="practice-title">
    <span class="line-primary">PSYCHOTHERAPY</span>
    <span class="line-secondary">PRACTICE</span>
  </h1>

  <section class="letter-body">
    <p>Lorem ipsum dolor sit amet, consectetur adipiscing elit. Fusce dignissim pretium consectetur. Curabitur tempor posuere massa in varius. Pellentesque viverra nibh eu vehicula mattis. Nullam porta facilisis justo, a feugiat dolor sodales sed. Vestibulum neque nisi, elementum tincidunt metus sit amet, egestas bibendum enim. Aenean a blandit elit, vel rutrum mi. Nunc dapibus turpis sed massa aliquet tincidunt.</p>
    <p>Pellentesque id neque ligula. Nullam posuere, ligula a mattis posuere, lacus nisl adipiscing nunc, eu congue justo est ut diam. Nam quam nibh, dignissim non consequat in, semper eget purus. Nulla arcu sapien, viverra vitae metus tempor, congue ornare diam.</p>
    <p>Pellentesque vel nibh tempus, ullamcorper tortor sed, bibendum augue. Phasellus sollicitudin justo et quam aliquam sollicitudin. Sed eget nibh mollis, mattis sem et, viverra nulla.</p>
  </section>

  <ul class="contact-list">
    <li><svg viewBox="0 0 24 24"><path d="M6.6 10.8a15.1 15.1 0 0 0 6.6 6.6l2.2-2.2a1 1 0 0 1 1-.25 11.4 11.4 0 0 0 3.6.57 1 1 0 0 1 1 1V20a1 1 0 0 1-1 1A17 17 0 0 1 3 4a1 1 0 0 1 1-1h3.5a1 1 0 0 1 1 1c0 1.25.2 2.45.57 3.57a1 1 0 0 1-.25 1z"/></svg>+00 1234 5XXX 9012</li>
    <li><svg viewBox="0 0 24 24"><path d="M2 5h20v14H2z M2 5l10 8 10-8" stroke="#fff" stroke-width="1.5"/></svg>your email space</li>
    <li><svg viewBox="0 0 24 24"><path d="M5 2l14 11h-7l4 8-3 1.5-4-8-4 4z"/></svg>website address here</li>
  </ul>

  <section class="signature">
    <p class="signer-name">Your Name</p>
    <p class="signer-role">Designation</p>
    <p class="signer-note">Lorem ipsum dolor sit amet</p>
  </section>
</main>
</body>
</html>
```